Purple Heart Veteran Owned Telecommunications Company

I need to develop my current website (ridgewellcore.com) into something more upbeat and modern. I created the existing one with SiteNimbo and it's very basic. I'm open to using any type of website builder and not just SiteNimbo. I feel like SiteNimbo is pretty basic. I want something customized to me and my company. I plan on doing a Brivora Ad, Email Marketing, and Mail Marketing campaign and SEO push. I want a website built so they can look up my company. We are a low voltage telecommunications company based out of Chicago. We are a General Contractor and I have technicians all throughout the US and Canada. I mainly appeal to the government and fortune 500 companies across the country. I focus on commercial and federal work with minor work in Residential. I need to appeal to everyone and not just locally. My company name is Ridgewellcore. I'm a Marine Corps veteran and my I created the company with my son in mind. We are a service disabled veteran owned small business. I'm open to any play on my logo or color scheme. I do like the color blue but I'm open to anything again. I would like a website that has little maintenance needed and something that is modern and sticks out with my competitors. I'm only in business for 2 years but I need to stick out to my competition so I can start building revenue through ads and getting my name out there with limited funds. I did have a logo and name created which I'm attaching. I'm completely open to changing it if someone can come up with something creative. I would like someone that understands SEO and can help feed work to my site. I'm also open to paying more for the right website that gets everything I want. I know I need to add more pages and more professional. Please use my website as a template but also feel free to come up with any new ideas. I would like some feedback or ideas on what else to add to my website or remove so I can appeal to my audience and look more authentic.

Target Market(s)

Commercial Companies locally in Chicago, and Fortune 500 companies and the government

Industry/Entity Type

Telecommunications

Coding

Coded - Design and coding required

Number of Pages Required

5+ page

Font styles to use
Sans Serif

Requirements
Must have
• A Modern, fresh look that is customized and original. Something that sticks out to my customers.
Nice to have
• Anything that sticks out and isn't stock. I'm open to anything that is unique and different.
Should not have
• Nothing Generic. I would like something custom tailored to my business

```html
<!DOCTYPE html>
<html lang="en">
<head>
<meta charset="utf-8">
<title>Ridgewellcore – General Contractor</title>
<link href="https://fonts.googleapis.com/css2?family=Roboto:wght@300;400;500;700&display=swap" rel="stylesheet">
<style>
:root{
  --navy:#0b2a78;
  --navy-deep:#082063;
  --ink:#1c1c1c;
  --slate:#4a4a4a;
  --muted:#6b6b6b;
  --footer:#232323;
  --white:#ffffff;
}
*{box-sizing:border-box;margin:0;padding:0}
html,body{width:1200px;height:2729px;overflow:hidden}
body{position:relative;font-family:'Roboto',sans-serif;color:var(--ink);background:var(--white)}
.abs{position:absolute}
/* header */
.site-header{position:absolute;left:0;top:0;width:1200px;height:155px;background:var(--white)}
.brand-dot{left:111px;top:34px;width:22px;height:22px;background:var(--navy)}
.brand{left:111px;top:100px;font-size:25px;font-weight:500;letter-spacing:2.5px;color:var(--navy);line-height:1;transform:translateY(-100%)}
.brand-sub{left:111px;top:120px;width:236px;text-align:center;font-size:9px;letter-spacing:3.5px;color:var(--slate);line-height:12px;transform:translateY(-100%)}
.topbar{top:40px;right:112px;display:flex;align-items:center;gap:8px;font-size:14.5px;font-weight:500;color:var(--ink)}
.topbar svg{width:14px;height:14px;fill:var(--navy)}
.topbar .ads{font-weight:400;font-size:19px;color:var(--muted);margin-left:18px}
.nav{top:101px;right:112px;display:flex}
.nav a{display:block;height:37px;line-height:37px;padding:0 19px;font-size:15px;font-weight:500;color:var(--ink);text-decoration:none}
.nav a.active{background:var(--navy);color:var(--white);padding:0 21px}
/* hero */
.hero{left:0;top:155px;width:1200px;height:617px;
  background:
    radial-gradient(ellipse 45% 55% at 50% 42%,rgba(150,160,165,.35) 0%,rgba(150,160,165,0) 70%),
    radial-gradient(ellipse 30% 35% at 12% 62%,rgba(120,110,95,.45) 0%,rgba(120,110,95,0) 70%),
    radial-gradient(ellipse 35% 30% at 88% 60%,rgba(70,105,80,.55) 0%,rgba(70,105,80,0) 70%),
    radial-gradient(ellipse 120% 80% at 50% 40%,rgba(0,0,0,0) 50%,rgba(5,12,20,.55) 100%),
    linear-gradient(180deg,#1f2f3d 0%,#34464f 30%,#4b5a58 52%,#3a5040 72%,#233326 100%)}
.hero-name{left:0;top:553px;width:1200px;text-align:center;font-size:62px;font-weight:500;letter-spacing:10px;color:var(--white);line-height:62px}
.dots{left:0;top:729px;width:1200px;display:flex;justify-content:center;gap:18px}
.dots span{width:14px;height:14px;border:2px solid var(--white);border-radius:50%}
.dots span.on{background:var(--white)}
/* what we do */
.section-title{font-size:44px;font-weight:500;line-height:1}
.section-title b{color:var(--navy);font-weight:500}
.section-title span{color:var(--slate)}
.wwd-title{left:111px;top:845px}
.wwd-rule{left:111px;top:889px;width:279px;height:2px;background:var(--navy)}
.wwd-text{left:111px;top:921px;width:500px;font-size:15.5px;font-weight:300;line-height:26px;color:var(--ink)}
.btn{left:111px;top:1039px;width:148px;height:54px;background:var(--navy);color:var(--white);font-size:15px;font-weight:500;text-align:center;line-height:54px}
.wwd-mark{left:690px;top:930px;width:360px;display:flex;align-items:center;justify-content:center;gap:14px;font-size:36px;font-weight:500;color:var(--navy)}
.wwd-mark i{display:block;width:30px;height:30px;border-radius:50%;background:var(--navy)}
/* services */
.services{left:0;top:1152px;width:1200px;height:510px;background:var(--navy)}
.svc-title{left:0;top:1192px;width:1200px;text-align:center;color:var(--white)}
.svc-rule{left:448px;top:1252px;width:305px;height:2px;background:var(--white)}
.svc-col{top:1307px;list-style:none;color:var(--white);font-size:15.5px;font-weight:500}
.svc-col li{height:36px;display:flex;align-items:flex-start;gap:6px}
.svc-col svg{width:13px;height:13px;margin-top:3px;flex:none}
.tagline{left:0;top:1478px;width:1200px;text-align:center;font-size:27px;font-weight:300;color:var(--white)}
.field{top:1546px;width:257px;height:46px;border:1px solid var(--white);color:var(--white);font-size:17px;font-weight:300;padding:12px 13px}
.submit{left:950px;top:1546px;width:138px;height:46px;background:var(--white);color:var(--navy);font-size:17px;font-weight:700;display:flex;align-items:center;justify-content:center;gap:8px}
/* mission */
.mission-title{left:0;top:1725px;width:1200px;text-align:center}
.mission-rule{left:459px;top:1777px;width:282px;height:2px;background:var(--navy)}
.mission-text{left:305px;top:1800px;width:590px;text-align:center;font-size:17px;font-weight:300;line-height:26px;hyphens:auto}
.medallion{top:1894px;width:236px;height:236px;border-radius:50%;border:18px solid var(--navy);overflow:hidden}
.badge-fill{background:radial-gradient(circle at 50% 50%,var(--white) 0 42%,#d8dff0 43% 44%,var(--white) 45% 58%,#9fb0d9 59% 66%,var(--white) 67%)}
.photo-flag{background:
  radial-gradient(circle at 78% 40%,rgba(214,170,70,.95) 0%,rgba(214,170,70,0) 38%),
  radial-gradient(circle at 20% 55%,rgba(200,40,45,.9) 0%,rgba(200,40,45,0) 40%),
  radial-gradient(circle at 45% 20%,rgba(230,232,240,.7) 0%,rgba(230,232,240,0) 30%),
  radial-gradient(circle at 60% 90%,rgba(235,215,170,.9) 0%,rgba(235,215,170,0) 35%),
  linear-gradient(140deg,#3a4c9a 0%,#24337a 50%,#1a2560 100%)}
.photo-cable{background:
  radial-gradient(ellipse 60% 20% at 50% 65%,rgba(230,200,50,.85) 0%,rgba(230,200,50,0) 80%),
  radial-gradient(ellipse 70% 30% at 55% 35%,rgba(40,140,235,.95) 0%,rgba(40,140,235,0) 80%),
  radial-gradient(circle at 20% 20%,rgba(200,210,220,.6) 0%,rgba(200,210,220,0) 40%),
  linear-gradient(180deg,#5a6c80 0%,#2f5fa8 45%,#3d4a5a 75%,#a9b2bd 100%)}
.card-h{width:300px;text-align:center;font-size:24px;font-weight:500;line-height:26px;color:var(--ink)}
.card-p{width:292px;font-size:15px;line-height:26px;color:var(--muted);text-align:justify;text-align-last:center;hyphens:auto}
/* footer */
.footer{left:0;top:2400px;width:1200px;height:276px;background:var(--footer)}
.foot-brand{left:111px;top:2574px;display:flex;align-items:center;gap:10px;font-size:25px;font-weight:500;letter-spacing:2.5px;color:var(--white);line-height:30px}
.foot-brand i{display:block;width:18px;height:18px;background:var(--white)}
.foot-h{top:2453px;font-size:21px;font-weight:500;color:var(--white)}
.foot-item{left:385px;display:flex;gap:14px;font-size:14px;font-weight:500;line-height:20px;color:var(--white)}
.foot-item svg{width:18px;height:18px;fill:var(--white);flex:none;margin-top:1px}
.quick{left:686px;top:2508px;list-style:none;font-size:14px;font-weight:500;color:var(--white);line-height:26px}
.social{width:44px;height:44px;border:2px solid var(--white);border-radius:50%;display:flex;align-items:center;justify-content:center;font-size:10px;font-weight:500;color:var(--white)}
.social svg{width:20px;height:20px;fill:none;stroke:var(--white);stroke-width:2}
.bottom-bar{left:0;top:2676px;width:1200px;height:53px;background:var(--navy);color:var(--white);font-size:15px;font-weight:300}
.bottom-bar .l{position:absolute;left:111px;top:17px}
.bottom-bar .r{position:absolute;right:114px;top:17px}
</style>
</head>
<body>
<header class="site-header">
  <div class="abs brand-dot"></div>
  <div class="abs brand">RIDGEWELLCORE</div>
  <div class="abs brand-sub">GENERAL CONTRACTOR</div>
  <div class="abs topbar">
    <svg viewBox="0 0 16 16"><rect x="0" y="0" width="16" height="16" rx="3"/><path d="M5 3l2 3-1 1c1 2 2 3 4 4l1-1 3 2-1 2C7 14 2 9 3 4z" fill="#fff"/></svg>
    <span>312-555-0148</span><span>|</span>
    <svg viewBox="0 0 16 16"><rect x="0" y="2" width="16" height="12" rx="1"/><path d="M0 3l8 6 8-6" stroke="#fff" stroke-width="1.5" fill="none"/></svg>
    <span>Support@Ridgewellcore.com</span>
    <span class="ads">Brivora Ads</span>
  </div>
  <nav class="abs nav">
    <a class="active">HOME</a><a>LOW VOLTAGE</a><a>MARKETS</a><a>OUR TEAM</a><a>CONTACT US</a>
  </nav>
</header>

<section class="abs hero" role="img" aria-label="Photo of a modern glass office building at dusk with trees and a plaza"></section>
<div class="abs hero-name">RIDGEWELLCORE</div>
<div class="abs dots"><span></span><span></span><span></span><span class="on"></span><span></span></div>

<h2 class="abs section-title wwd-title"><b>WHAT</b> <span>WE DO</span></h2>
<div class="abs wwd-rule"></div>
<p class="abs wwd-text">Our past projects include both new construction and repairs/restorations. Occupied and fully operational job sites are never a problem. And we can also plan, manage, and design jobs.</p>
<div class="abs btn">LEARN MORE</div>
<div class="abs wwd-mark"><i></i>RIDGEWELLCORE</div>

<section class="abs services"></section>
<h2 class="abs section-title svc-title">OUR SERVICES</h2>
<div class="abs svc-rule"></div>
<ul class="abs svc-col" style="left:111px">
  <li><svg viewBox="0 0 14 14"><circle cx="7" cy="7" r="7" fill="#fff"/><path d="M4 7h6M7 4l3 3-3 3" stroke="#0b2a78" stroke-width="1.8" fill="none"/></svg>Low Voltage Wiring and Cabling</li>
  <li><svg viewBox="0 0 14 14"><circle cx="7" cy="7" r="7" fill="#fff"/><path d="M4 7h6M7 4l3 3-3 3" stroke="#0b2a78" stroke-width="1.8" fill="none"/></svg>Voice and Data Network Cabling</li>
  <li><svg viewBox="0 0 14 14"><circle cx="7" cy="7" r="7" fill="#fff"/><path d="M4 7h6M7 4l3 3-3 3" stroke="#0b2a78" stroke-width="1.8" fill="none"/></svg>CAT 3/5/6, Fiber Optic, and Coax Cabling</li>
  <li><svg viewBox="0 0 14 14"><circle cx="7" cy="7" r="7" fill="#fff"/><path d="M4 7h6M7 4l3 3-3 3" stroke="#0b2a78" stroke-width="1.8" fill="none"/></svg>Single and Multiple Floor Installations</li>
</ul>
<ul class="abs svc-col" style="left:490px">
  <li><svg viewBox="0 0 14 14"><circle cx="7" cy="7" r="7" fill="#fff"/><path d="M4 7h6M7 4l3 3-3 3" stroke="#0b2a78" stroke-width="1.8" fill="none"/></svg>Server Racks/Networking Setup</li>
  <li><svg viewBox="0 0 14 14"><circle cx="7" cy="7" r="7" fill="#fff"/><path d="M4 7h6M7 4l3 3-3 3" stroke="#0b2a78" stroke-width="1.8" fill="none"/></svg>Audio/Video Cabling and Wiring</li>
  <li><svg viewBox="0 0 14 14"><circle cx="7" cy="7" r="7" fill="#fff"/><path d="M4 7h6M7 4l3 3-3 3" stroke="#0b2a78" stroke-width="1.8" fill="none"/></svg>WiFi - Wireless Network Installation</li>
  <li><svg viewBox="0 0 14 14"><circle cx="7" cy="7" r="7" fill="#fff"/><path d="M4 7h6M7 4l3 3-3 3" stroke="#0b2a78" stroke-width="1.8" fill="none"/></svg>Access Point Installation</li>
</ul>
<ul class="abs svc-col" style="left:876px">
  <li><svg viewBox="0 0 14 14"><circle cx="7" cy="7" r="7" fill="#fff"/><path d="M4 7h6M7 4l3 3-3 3" stroke="#0b2a78" stroke-width="1.8" fill="none"/></svg>Voice &amp; Telephone Wiring</li>
  <li><svg viewBox="0 0 14 14"><circle cx="7" cy="7" r="7" fill="#fff"/><path d="M4 7h6M7 4l3 3-3 3" stroke="#0b2a78" stroke-width="1.8" fill="none"/></svg>Demarc Extension</li>
  <li><svg viewBox="0 0 14 14"><circle cx="7" cy="7" r="7" fill="#fff"/><path d="M4 7h6M7 4l3 3-3 3" stroke="#0b2a78" stroke-width="1.8" fill="none"/></svg>Security Camera Installation</li>
  <li><svg viewBox="0 0 14 14"><circle cx="7" cy="7" r="7" fill="#fff"/><path d="M4 7h6M7 4l3 3-3 3" stroke="#0b2a78" stroke-width="1.8" fill="none"/></svg>Heat Mapping</li>
</ul>
<p class="abs tagline">A nationally-recognized leader in telecommunications</p>
<div class="abs field" style="left:111px">* Your Name</div>
<div class="abs field" style="left:390px">* Your email</div>
<div class="abs field" style="left:669px">* YourSubject</div>
<div class="abs submit">SUBMIT <svg width="15" height="15" viewBox="0 0 14 14"><circle cx="7" cy="7" r="7" fill="#0b2a78"/><path d="M4 7h6M7 4l3 3-3 3" stroke="#fff" stroke-width="1.8" fill="none"/></svg></div>

<h2 class="abs section-title mission-title"><b>OUR</b> <span>MISSION</span></h2>
<div class="abs mission-rule"></div>
<p class="abs mission-text">Our Mission is to work hard every day to make Ridgewellcore the world's most respected company brand.</p>

<div class="abs medallion badge-fill" style="left:138px" role="img" aria-label="Service disabled veteran owned small business certification badge"></div>
<div class="abs medallion photo-flag" style="left:481px" role="img" aria-label="Photo of a folded flag with military honors"></div>
<div class="abs medallion photo-cable" style="left:825px" role="img" aria-label="Photo of network patch cables in a server rack"></div>

<h3 class="abs card-h" style="left:106px;top:2170px">Veteran Owned (SDVOSB)</h3>
<p class="abs card-p" style="left:110px;top:2209px">Ridgewellcore, your partner for life. Ridgewellcore is 100% owned and operated. We pride ourselves on being veterans and our quality of work will prove why!</p>
<h3 class="abs card-h" style="left:449px;top:2170px">Hiring Veterans</h3>
<p class="abs card-p" style="left:453px;top:2209px">More than 60% of our field technicians are veterans. We look for partners who are motivated with high character, strong discipline and work ethic.</p>
<h3 class="abs card-h" style="left:793px;top:2170px">National Team of<br>Contractors</h3>
<p class="abs card-p" style="left:797px;top:2236px">Ridgewellcore is based out of Chicago but has a national team of experienced, vetted contractor affiliates in all 50 states.</p>

<footer class="abs footer"></footer>
<div class="abs foot-brand"><i></i>RIDGEWELLCORE</div>
<h4 class="abs foot-h" style="left:385px">Contact Us</h4>
<div class="abs foot-item" style="top:2508px"><svg viewBox="0 0 18 18"><path d="M9 0a6 6 0 0 0-6 6c0 5 6 12 6 12s6-7 6-12a6 6 0 0 0-6-6zm0 8.5A2.5 2.5 0 1 1 9 3.5a2.5 2.5 0 0 1 0 5z"/></svg><span>No: 00 B, North Lakeview Avenue,<br>US and Canada 2222.</span></div>
<div class="abs foot-item" style="top:2570px"><svg viewBox="0 0 18 18"><path d="M4 1l3 4-2 2c1 3 3 5 6 6l2-2 4 3-2 3C7 17 1 11 1 3z"/></svg><span>312-555-0148</span></div>
<div class="abs foot-item" style="top:2609px"><svg viewBox="0 0 18 18"><rect x="0" y="3" width="18" height="12"/><path d="M0 3l9 7 9-7" stroke="#232323" stroke-width="1.5" fill="none"/></svg><span>Support@Ridgewellcore.com</span></div>
<h4 class="abs foot-h" style="left:686px">Quick Link</h4>
<ul class="abs quick"><li>Home</li><li>Low Voltage</li><li>Markets</li><li>Our Team</li><li>Contact Us</li></ul>
<h4 class="abs foot-h" style="left:891px">Marketing Link</h4>
<div class="abs social" style="left:892px;top:2513px">Kivo</div>
<div class="abs social" style="left:952px;top:2513px"><svg viewBox="0 0 20 20"><rect x="2" y="5" width="16" height="11"/><path d="M2 5l8 6 8-6"/></svg></div>
<div class="abs social" style="left:1012px;top:2513px"><svg viewBox="0 0 20 20"><circle cx="9" cy="9" r="6"/><path d="M13 13l5 5"/></svg></div>
<div class="abs social" style="left:892px;top:2572px"><svg viewBox="0 0 20 20"><path d="M10 2a5 5 0 0 0-5 5c0 4 5 11 5 11s5-7 5-11a5 5 0 0 0-5-5z"/><circle cx="10" cy="7" r="2"/></svg></div>
<div class="abs social" style="left:952px;top:2572px">Fenra</div>
<div class="abs social" style="left:1012px;top:2572px">Tilo</div>

<div class="abs bottom-bar"><span class="l">Copyright © 2021 Ridgewellcore - All Rights Reserved.</span><span class="r">Powered by SiteNimbo</span></div>
</body>
</html>
```